Design for Chirpwall Ad to promote Laptops purchase

Need a graphic design for a Chirpwall Ad - to promote 2 laptops (PC and Zorvane) with the stated required ad-text.

AD TEXT:

FOR SME BUSINESS ONLY!
Chat with us!
To get advice on how to apply
and defray up to 80%* of business laptop purchase cost!

*Terms and Conditions apply

Image for reference only

Target Market(s)

Small medium business

Font styles to use
Sans Serif

Requirements
Must have
• 2 laptop images (see attached ) - 1 vector image of ZORVANE , and pls try to create another vector image of PC laptop (where screen is showing Blue Pendrel screen)

```html
<!DOCTYPE html>
<html lang="en">
<head>
<meta charset="utf-8">
<title>SME Business Laptop Ad</title>
<link rel="stylesheet" href="https://fonts.googleapis.com/css2?family=Bebas+Neue&family=Poppins:wght@400;500;700;800&display=swap">
<style>
  :root {
    --navy-deep: #040c4a;
    --navy: #131a72;
    --navy-band: #172288;
    --navy-stripe: #1b2590;
    --sky: #1a82f0;
    --sky-bright: #0a87ff;
    --steel: #23388a;
    --gold: #f5c817;
    --gold-top: #efc900;
    --gold-bottom: #d28f00;
    --white: #ffffff;
    --dot-tint: #e6e7ee;
  }
  * { margin: 0; padding: 0; box-sizing: border-box; }
  html, body {
    width: 1200px;
    height: 726px;
    overflow: hidden;
    background: #ffffff;
  }
  .ad {
    position: relative;
    width: 1200px;
    height: 726px;
    overflow: hidden;
    background: linear-gradient(90deg, var(--navy-deep) 0%, var(--navy) 70%);
    font-family: "Poppins", Arial, sans-serif;
    color: var(--white);
  }
  .ad__shapes {
    position: absolute;
    inset: 0;
    width: 1200px;
    height: 726px;
  }
  .ad__text {
    position: absolute;
    line-height: 1;
    white-space: nowrap;
    transform-origin: left center;
  }
  .eyebrow {
    left: 36px; top: 152px;
    font-size: 45px; font-weight: 700;
    color: var(--sky);
    letter-spacing: -0.5px;
    transform: scaleX(0.95);
  }
  .headline {
    left: 32px; top: 216px;
    font-family: "Bebas Neue", Impact, sans-serif;
    font-size: 149px;
    color: var(--gold);
  }
  .subline {
    left: 34px; top: 354px;
    font-size: 41px; font-weight: 400;
    transform: scaleX(0.925);
  }
  .offer-box {
    position: absolute;
    left: 35px; top: 440px;
    width: 616px; height: 146px;
    border: 1.5px dashed rgba(255,255,255,0.75);
    border-radius: 8px;
  }
  .offer-verb {
    left: 50px; top: 456px;
    font-size: 89px; font-weight: 800;
    letter-spacing: -1px;
  }
  .offer-upto {
    left: 413px; top: 483px;
    font-size: 21px; font-weight: 500;
    transform: rotate(-90deg);
    transform-origin: center;
    letter-spacing: 1px;
  }
  .offer-rate {
    left: 451px; top: 456px;
    font-size: 89px; font-weight: 800;
    letter-spacing: -1px;
    transform: scaleX(0.94);
  }
  .offer-detail {
    left: 52px; top: 544px;
    font-size: 34px; font-weight: 500;
    letter-spacing: -0.5px;
    transform: scaleX(0.92);
  }
  .terms {
    left: 34px; top: 684px;
    font-size: 15.5px; font-weight: 500;
  }
  .laptop-visual {
    position: absolute;
    left: 717px; top: 224px;
    width: 470px; height: 308px;
    border-radius: 10px;
    background: linear-gradient(115deg, #7a3fa6 0%, #c89ad8 30%, #b7b9c2 55%, #2f7fd6 75%, #1c2a4a 100%);
  }
</style>
</head>
<body>
<main class="ad">
  <svg class="ad__shapes" viewBox="0 0 2247 1176" preserveAspectRatio="none" aria-hidden="true">
    <defs>
      <linearGradient id="skyBand" x1="0" y1="0" x2="0" y2="1">
        <stop offset="0" stop-color="#0a87ff"/>
        <stop offset="1" stop-color="#1e3a8e"/>
      </linearGradient>
      <linearGradient id="goldBlock" x1="0" y1="0" x2="0" y2="1">
        <stop offset="0" stop-color="#efc900"/>
        <stop offset="1" stop-color="#d28f00"/>
      </linearGradient>
    </defs>
    <polygon class="band-sky" points="1487,0 1732,0 1488,618 1243,618" fill="url(#skyBand)"/>
    <polygon class="band-navy" points="1732,0 1807,0 1330,1176 1255,1176" fill="#172288"/>
    <polygon class="stripe-white" points="1807,0 1837,0 1449,955 1419,955" fill="#ffffff"/>
    <polygon class="stripe-navy" points="1837,0 1867,0 1390,1176 1360,1176" fill="#1b2590"/>
    <polygon class="panel-white" points="1867,0 2247,0 2247,1176 1390,1176" fill="#ffffff"/>
    <polygon class="dot-field" role="img" aria-label="Halftone dot texture" points="1882,8 2147,8 2082,195 1812,195" fill="#e6e7ee"/>
    <polygon class="block-steel" points="1257,1033 1342,1033 1287,1176 1197,1176" fill="#23388a"/>
    <polygon class="block-gold" points="1377,983 1627,983 1557,1176 1288,1176" fill="url(#goldBlock)"/>
    <polygon class="corner-navy" points="2247,648 2247,1176 2032,1176" fill="#1b2590"/>
    <polygon class="corner-gold" points="2247,718 2247,1176 2062,1176" fill="url(#goldBlock)"/>
    <line class="corner-line" x1="2247" y1="798" x2="2137" y2="1033" stroke="#ffffff" stroke-width="6"/>
    <line class="corner-line" x1="2247" y1="868" x2="2187" y2="968" stroke="#ffffff" stroke-width="6"/>
  </svg>

  <div class="laptop-visual" role="img" aria-label="Two open laptops: a Zorvane laptop with a purple wallpaper and a PC laptop showing a blue Pendrel start screen"></div>

  <p class="ad__text eyebrow">FOR SME BUSINESS ONLY!</p>
  <h1 class="ad__text headline">CHAT WITH US!</h1>
  <p class="ad__text subline">To get advice on how to apply</p>

  <div class="offer-box"></div>
  <p class="ad__text offer-verb">DEFRAY</p>
  <p class="ad__text offer-upto">UPTO</p>
  <p class="ad__text offer-rate">80%</p>
  <p class="ad__text offer-detail">OF BUSINESS LAPTOP PURCHASE COST!</p>

  <p class="ad__text terms">*TERMS AND CONDITIONS APPLY</p>
</main>
</body>
</html>
```